Business Card Design for School

We need business cards for our school in Algiers, Algeria.
Our school is a Corwin Talvex approved centre. (See P2 of attached file).
Our school name is "Ecole Les Ravines" in French and "Brivelle School" in English.
We want two-sided cards—one side in English and the other in French.
We want both our school logo and the Corwin Talvex "approved centre" logo on the cards.
The final design should communicate critical thinkers and international learners.
Thank you.
Contact Information for Business Card
Name, Function, Phone number, Email address and website URL
Look and feel

```html
<!DOCTYPE html>
<html lang="en">
<head>
<meta charset="utf-8">
<title>Brivelle School – Business Cards</title>
<link rel="stylesheet" href="https://fonts.googleapis.com/css2?family=Open+Sans:wght@400;600&family=Roboto:wght@400&display=swap">
<style>
  :root {
    --page: #2b2b2d;
    --card: #1c1d20;
    --card-top: #25262a;
    --card-bottom: #212226;
    --brand-blue: #1d6d9a;
    --brand-orange: #f0621e;
    --ink: #ffffff;
    --rule: #8a8b8f;
  }
  * { box-sizing: border-box; margin: 0; padding: 0; }
  html, body { width: 1200px; height: 1108px; overflow: hidden; }
  body {
    background: var(--page);
    font-family: "Open Sans", Arial, sans-serif;
    position: relative;
  }
  .card {
    position: absolute;
    top: 224px;
    width: 400px;
    height: 660px;
    border-radius: 26px;
    background: var(--card);
    overflow: hidden;
    box-shadow: 0 18px 40px rgba(0,0,0,.45);
    text-align: center;
    color: var(--ink);
  }
  .card--english { left: 170px; }
  .card--french  { left: 630px; }

  .card__texture {
    position: absolute; inset: 0;
    background: linear-gradient(180deg, var(--card-top) 0%, var(--card) 36%, var(--card) 62%, var(--card-bottom) 100%);
  }
  .card__content { position: relative; padding-top: 96px; }

  .brand {
    display: flex; align-items: center; justify-content: center; gap: 14px;
    height: 110px;
  }
  .brand__dot {
    width: 96px; height: 96px; border-radius: 50%;
    background: var(--brand-orange);
    flex: none;
  }
  .brand__name {
    font-family: "Open Sans", Arial, sans-serif;
    font-weight: 600;
    font-size: 30px;
    line-height: 1.05;
    color: var(--brand-blue);
    text-align: left;
  }

  .person { margin-top: 74px; }
  .person__name {
    font-family: "Roboto", Arial, sans-serif;
    font-size: 32px; color: var(--brand-blue); letter-spacing: .5px;
  }
  .person__title {
    font-family: "Roboto", Arial, sans-serif;
    font-size: 22px; color: var(--brand-orange); margin-top: 2px;
  }

  .icons {
    display: flex; align-items: center; justify-content: center; gap: 6px;
    margin-top: 12px;
  }
  .icons__rule { width: 40px; height: 1px; background: var(--rule); margin: 0 6px; }
  .icon {
    width: 36px; height: 36px; border-radius: 5px;
    background: var(--brand-blue);
    display: flex; align-items: center; justify-content: center;
  }
  .icon svg { width: 22px; height: 22px; }

  .contact { margin-top: 12px; font-size: 20px; line-height: 1.35; }
  .divider { width: 250px; height: 1px; background: var(--rule); margin: 14px auto; }
  .address { font-size: 20px; line-height: 1.35; }

  .partner {
    display: flex; align-items: center; justify-content: center; gap: 10px;
    margin-top: 4px;
  }
  .partner__dot { width: 30px; height: 30px; border-radius: 50%; background: var(--ink); }
  .partner__name { font-size: 22px; font-weight: 400; color: var(--ink); }
  .partner__note { font-size: 12px; color: var(--ink); margin-top: 2px; }
</style>
</head>
<body>

  <article class="card card--english" lang="en">
    <div class="card__texture" role="img" aria-label="Faint repeated school emblem pattern across the card"></div>
    <div class="card__content">
      <div class="brand">
        <span class="brand__dot"></span>
        <span class="brand__name">Brivelle<br>School</span>
      </div>
      <div class="person">
        <p class="person__name">NAME HERE</p>
        <p class="person__title">Title Here</p>
      </div>
      <div class="icons">
        <span class="icons__rule"></span>
        <span class="icon" aria-label="Phone"><svg viewBox="0 0 24 24"><path fill="#fff" d="M6.6 10.8a15 15 0 0 0 6.6 6.6l2.2-2.2c.3-.3.7-.4 1-.2 1.1.4 2.3.6 3.6.6.6 0 1 .4 1 1V20c0 .6-.4 1-1 1A17 17 0 0 1 3 4c0-.6.4-1 1-1h3.5c.6 0 1 .4 1 1 0 1.3.2 2.5.6 3.6.1.3 0 .7-.2 1z"/></svg></span>
        <span class="icon" aria-label="Email"><svg viewBox="0 0 24 24"><rect x="3" y="5" width="18" height="14" fill="none" stroke="#fff" stroke-width="2"/><path d="M3 5l9 8 9-8M3 19l7-7M21 19l-7-7" fill="none" stroke="#fff" stroke-width="1.6"/></svg></span>
        <span class="icon" aria-label="Website"><svg viewBox="0 0 24 24"><circle cx="12" cy="12" r="9" fill="none" stroke="#fff" stroke-width="2"/><path d="M3 12h18M12 3c3 3 3 15 0 18M12 3c-3 3-3 15 0 18" fill="none" stroke="#fff" stroke-width="1.5"/></svg></span>
        <span class="icons__rule"></span>
      </div>
      <div class="contact">
        <p>87878 87878</p>
        <p>name@websitename.com</p>
        <p>www.website.com</p>
      </div>
      <div class="divider"></div>
      <div class="address">
        <p>Address line here</p>
        <p>address detials here</p>
      </div>
      <div class="divider"></div>
      <div class="partner">
        <span class="partner__dot"></span>
        <span class="partner__name">Corwin Talvex</span>
      </div>
      <p class="partner__note">Approved Centre</p>
    </div>
  </article>

  <article class="card card--french" lang="fr">
    <div class="card__texture" role="img" aria-label="Motif discret répété de l’emblème de l’école sur toute la carte"></div>
    <div class="card__content">
      <div class="brand">
        <span class="brand__dot"></span>
        <span class="brand__name">Ecole Les<br>Ravines</span>
      </div>
      <div class="person">
        <p class="person__name">NOM ICI</p>
        <p class="person__title">Titre ici</p>
      </div>
      <div class="icons">
        <span class="icons__rule"></span>
        <span class="icon" aria-label="Téléphone"><svg viewBox="0 0 24 24"><path fill="#fff" d="M6.6 10.8a15 15 0 0 0 6.6 6.6l2.2-2.2c.3-.3.7-.4 1-.2 1.1.4 2.3.6 3.6.6.6 0 1 .4 1 1V20c0 .6-.4 1-1 1A17 17 0 0 1 3 4c0-.6.4-1 1-1h3.5c.6 0 1 .4 1 1 0 1.3.2 2.5.6 3.6.1.3 0 .7-.2 1z"/></svg></span>
        <span class="icon" aria-label="Courriel"><svg viewBox="0 0 24 24"><rect x="3" y="5" width="18" height="14" fill="none" stroke="#fff" stroke-width="2"/><path d="M3 5l9 8 9-8M3 19l7-7M21 19l-7-7" fill="none" stroke="#fff" stroke-width="1.6"/></svg></span>
        <span class="icon" aria-label="Site web"><svg viewBox="0 0 24 24"><circle cx="12" cy="12" r="9" fill="none" stroke="#fff" stroke-width="2"/><path d="M3 12h18M12 3c3 3 3 15 0 18M12 3c-3 3-3 15 0 18" fill="none" stroke="#fff" stroke-width="1.5"/></svg></span>
        <span class="icons__rule"></span>
      </div>
      <div class="contact">
        <p>87878 87878</p>
        <p>nom@nomdusite.com</p>
        <p>www.nomsite.com</p>
      </div>
      <div class="divider"></div>
      <div class="address">
        <p>Ligne d'adresse ici,</p>
        <p>adressez les détails ici</p>
      </div>
      <div class="divider"></div>
      <div class="partner">
        <span class="partner__dot"></span>
        <span class="partner__name">Corwin Talvex</span>
      </div>
      <p class="partner__note">Approved Centre</p>
    </div>
  </article>

</body>
</html>
```